Discreet simple classy for adult entertainment

I would like a matte black business card with gold writing for my business. Keeping it simple. Having my following:

Lana frost
Events. Entertainment. Promotions
0491726580

or alternatively could have what i had on my previous card below but i think i prefer the above as again - discretion.

Maybe a nice gold line thru the card or some other very simple design . Or not open to ideas/ can be doublesided if any good ideas with that.

included pics of my old bus card. not sure weather i want a photo on it or not. if i do it wont be the same pic. i kinda wanted a card that was discreet so if it was in someones wallet they wouldn't neccessarily realise it was from a stripper.

Target Market(s)

men

Industry/Entity Type

Business

Contact Information for Business Card

Lana frost
0491726580

Requirements
Nice to have
• i don't know i am really open to anything. im giving my cards to guys so something they can have in their wallet that is discreet preferably.

```html
<!DOCTYPE html>
<html lang="en">
<head>
<meta charset="utf-8">
<title>Lana Frost – Business Card</title>
<link rel="stylesheet" href="https://fonts.googleapis.com/css2?family=Josefin+Sans:wght@300;400&display=swap">
<style>
  :root {
    --backdrop: #1c1c1e;
    --card-black: #111112;
    --gold: #c9974a;
    --photo-dark: #3a3a3a;
    --photo-mid: #5c5c5c;
    --photo-light: #8a8a8a;
  }
  * { box-sizing: border-box; margin: 0; padding: 0; }
  html, body {
    width: 1200px;
    height: 723px;
    overflow: hidden;
    background: var(--backdrop);
    font-family: "Josefin Sans", "Helvetica Neue", Arial, sans-serif;
  }
  .sheet {
    position: relative;
    width: 1200px;
    height: 723px;
    display: flex;
    align-items: center;
    justify-content: center;
    gap: 60px;
  }
  .card {
    position: relative;
    width: 525px;
    height: 300px;
    background: var(--card-black);
    overflow: hidden;
    color: var(--gold);
  }

  /* Front side */
  .card-front {
    display: flex;
    flex-direction: column;
    align-items: center;
    justify-content: center;
    text-align: center;
  }
  .card-front .name {
    font-weight: 400;
    font-size: 34px;
    letter-spacing: 0.16em;
    text-transform: uppercase;
    margin-bottom: 14px;
  }
  .card-front .divider {
    display: block;
    margin-bottom: 16px;
  }
  .card-front .services {
    font-weight: 300;
    font-size: 15px;
    letter-spacing: 0.14em;
    text-transform: uppercase;
    margin-bottom: 8px;
  }
  .card-front .phone {
    font-weight: 300;
    font-size: 15px;
    letter-spacing: 0.14em;
    margin-bottom: 30px;
  }
  .card-front .social {
    display: flex;
    align-items: center;
    gap: 6px;
    font-weight: 300;
    font-size: 12px;
    letter-spacing: 0.1em;
  }
  .card-front .social-dot {
    width: 6px;
    height: 6px;
    border-radius: 50%;
    background: var(--gold);
  }

  /* Back side */
  .card-back .photo {
    position: absolute;
    inset: 0;
    background: radial-gradient(ellipse at 35% 55%, var(--photo-light) 0%, var(--photo-mid) 40%, var(--photo-dark) 100%);
  }
  .card-back .roles {
    position: absolute;
    top: 24px;
    right: 34px;
    height: 252px;
    list-style: none;
    writing-mode: vertical-rl;
    display: flex;
    flex-direction: column;
    gap: 2px;
  }
  .card-back .roles li {
    font-weight: 300;
    font-size: 14px;
    letter-spacing: 0.08em;
    text-transform: uppercase;
    color: var(--gold);
    line-height: 24px;
    white-space: nowrap;
  }
  .card-back .roles li:nth-child(2) { padding-block-start: 14px; }
  .card-back .roles li:nth-child(3) { padding-block-start: 28px; }
  .card-back .roles li:nth-child(4) { padding-block-start: 110px; }
  .card-back .roles li:nth-child(5) { padding-block-start: 124px; }
</style>
</head>
<body>
  <main class="sheet">
    <section class="card card-back">
      <div class="photo" role="img" aria-label="Black and white photograph of a woman posing outdoors"></div>
      <ul class="roles">
        <li>Bikini Barmaid</li>
        <li>Poker Dealer</li>
        <li>Professional Party</li>
        <li>Waitress</li>
        <li>Strip Shows</li>
      </ul>
    </section>

    <section class="card card-front">
      <h1 class="name">Lana Frost</h1>
      <svg class="divider" width="130" height="6" viewBox="0 0 130 6" aria-hidden="true">
        <line x1="0" y1="3" x2="130" y2="3" stroke="#c9974a" stroke-width="1"/>
        <circle cx="65" cy="3" r="2" fill="#c9974a"/>
      </svg>
      <p class="services">Events. Entertainment. Promotions</p>
      <p class="phone">0491726580</p>
      <p class="social"><span class="social-dot"></span>@lanafrost</p>
    </section>
  </main>
</body>
</html>
```